Everything fresh, everything new

When I take over the practice, I would like to breathe new life into the practice. I want a business card design that catches the eye and brings a breath of fresh air

```html
<!DOCTYPE html>
<html lang="en">
<head>
<meta charset="utf-8">
<title>Praxisraum – Business Card</title>
<link rel="stylesheet" href="https://fonts.googleapis.com/css2?family=Lato:wght@400;700;900&display=swap">
<style>
  :root{
    --bg:#e6e7e8;
    --card-dark:#444446;
    --ink:#3a3a3c;
    --ink-soft:#5a5a5c;
    --green:#7cc230;
    --white:#ffffff;
    --faint:#eeeeef;
  }
  *{margin:0;padding:0;box-sizing:border-box}
  html,body{width:1200px;height:952px;overflow:hidden;background:var(--bg);font-family:'Lato',sans-serif}
  .stage{position:relative;width:1200px;height:952px}
  .card{position:absolute;top:316px;width:540px;height:320px;border-radius:22px;overflow:hidden;box-shadow:0 10px 30px rgba(0,0,0,.18)}
  .card--front{left:40px;background:var(--white)}
  .card--back{left:620px;background:var(--card-dark)}
  .front-shape{position:absolute;inset:0}

  .brand{position:absolute;display:flex;align-items:center;gap:10px}
  .brand__dot{width:16px;height:16px;border-radius:50%;background:var(--green)}
  .brand__name{font-weight:400;letter-spacing:.5px;white-space:nowrap}

  .card--front .brand{left:38px;top:50px}
  .card--front .brand__name{font-size:36px;color:var(--ink)}

  .person{position:absolute;left:290px;top:96px}
  .person__name{font-size:20px;font-weight:400;color:var(--ink);letter-spacing:1px;white-space:nowrap}
  .person__name b{font-weight:900;color:var(--green)}
  .person__role{font-size:14px;color:var(--ink-soft);margin-top:2px}
  .person__rule{width:46px;height:2px;background:var(--ink-soft);margin-top:8px}

  .contacts{position:absolute;left:232px;top:160px;list-style:none}
  .contacts li{display:flex;align-items:flex-start;gap:9px;font-size:12.5px;color:var(--ink);line-height:1.3;margin-bottom:7px;white-space:nowrap}
  .contacts .icon{flex:none;width:16px;height:16px;border-radius:3px;background:var(--ink);display:flex;align-items:center;justify-content:center}
  .contacts .icon--pin{background:var(--green)}

  .card--back .brand{left:50%;top:50%;transform:translate(-50%,-50%)}
  .card--back .brand__dot{width:22px;height:22px}
  .card--back .brand__name{font-size:44px;color:var(--white)}
</style>
</head>
<body>
<main class="stage">
  <section class="card card--front" aria-label="Business card front">
    <svg class="front-shape" viewBox="0 0 540 320" aria-hidden="true">
      <path d="M90,320 C60,230 90,110 200,70 C260,48 320,50 370,70" fill="none" stroke="var(--faint)" stroke-width="10"/>
      <path d="M540,100 C535,230 440,312 235,320 L540,320 Z" fill="var(--card-dark)"/>
      <path d="M540,100 C535,230 440,312 235,320" fill="none" stroke="var(--green)" stroke-width="9"/>
      <path d="M528,96 C520,200 450,280 330,300" fill="none" stroke="var(--green)" stroke-width="3"/>
    </svg>

    <div class="brand">
      <span class="brand__dot"></span>
      <span class="brand__name">Praxisraum</span>
    </div>

    <div class="person">
      <p class="person__name">JONAS M. <b>WEBER</b></p>
      <p class="person__role">Managing Director</p>
      <div class="person__rule"></div>
    </div>

    <ul class="contacts">
      <li><span class="icon icon--pin"><svg width="10" height="12" viewBox="0 0 10 12"><path d="M5 0C2.2 0 0 2.2 0 4.8 0 8 5 12 5 12s5-4 5-7.2C10 2.2 7.8 0 5 0z" fill="#fff"/><circle cx="5" cy="4.8" r="1.8" fill="var(--green)"/></svg></span><span>2175 Lindenhof Avenue<br>Marlow, MA 01842</span></li>
      <li><span class="icon"><svg width="10" height="10" viewBox="0 0 10 10"><path d="M2 0l2 2.5-1.2 1.2c.6 1.4 1.7 2.5 3.1 3.1L7.1 5.6 10 7.6 8.8 9.6C4.5 9.6.4 5.5.4 1.2z" fill="#fff"/></svg></span><span>+00 987 654 32</span></li>
      <li><span class="icon"><svg width="10" height="8" viewBox="0 0 10 8"><rect x=".5" y=".5" width="9" height="7" fill="none" stroke="#fff"/><path d="M.5.5 5 4.5 9.5.5" fill="none" stroke="#fff"/></svg></span><span>hello@praxisraum-mail.com</span></li>
      <li><span class="icon"><svg width="10" height="10" viewBox="0 0 10 10"><circle cx="5" cy="5" r="4.2" fill="none" stroke="#fff"/><path d="M.8 5h8.4M5 .8c-2 2.5-2 5.9 0 8.4M5 .8c2 2.5 2 5.9 0 8.4" fill="none" stroke="#fff" stroke-width=".8"/></svg></span><span>www.praxisraum-web.com</span></li>
    </ul>
  </section>

  <section class="card card--back" aria-label="Business card back">
    <div class="brand">
      <span class="brand__dot"></span>
      <span class="brand__name">Praxisraum</span>
    </div>
  </section>
</main>
</body>
</html>
```